Agricultural Consulting Website

Provide a modern yet business like website for my new Agriculture Consulting Business in Australia called FenTrove. Whilst we are based in Australia we are targetting both domestic and international markets (especially in Asia). We are targetting corporate, small business, government and farmer clients. The design should compliment our logo also sourced through pixel guild. The webiste should be easy for me to keep updated on a regular basis without the need to go back to the designer.

Industry/Entity Type

Business

Requirements
Must have
• clean crisp feel
• be modern yet business like
• be able to be updated by myself easily

```html
<!DOCTYPE html>
<html lang="en">
<head>
<meta charset="utf-8">
<title>FenTrove – Agricultural Consulting</title>
<link rel="stylesheet" href="https://fonts.googleapis.com/css2?family=Questrial&family=Arimo:wght@400;700&display=swap">
<style>
  :root {
    --soil: #5b2a0b;
    --soil-dark: #3e1c06;
    --leaf: #5a9a0c;
    --leaf-bright: #6fae12;
    --leaf-text: #5f9b10;
    --night: #1d2410;
    --bark: #6b2e0a;
    --ink: #222;
    --muted: #444;
    --white: #fff;
    --rule: #c8c8c8;
    --berry: #b0301c;
  }
  * { box-sizing: border-box; margin: 0; padding: 0; }
  html, body { width: 1200px; height: 796px; overflow: hidden; }
  body {
    background: linear-gradient(90deg, var(--soil-dark) 0, var(--soil) 12%, var(--soil) 88%, var(--soil-dark) 100%);
    font-family: "Questrial", "Arimo", sans-serif;
    color: var(--ink);
    position: relative;
  }
  .site { position: absolute; left: 120px; top: 0; width: 960px; height: 796px; }

  /* Header */
  .masthead { position: relative; height: 250px; background: linear-gradient(180deg, #5d9d0e 0, #4f8c08 100%); overflow: hidden; }
  .topbar { position: absolute; left: 0; right: 0; top: 0; height: 46px; background: linear-gradient(180deg, rgba(20,30,8,.9), rgba(30,45,10,.75)); }
  .main-nav { position: absolute; right: 20px; top: 14px; display: flex; gap: 19px; list-style: none; }
  .main-nav a { color: #c9d3b8; font-size: 14.5px; text-decoration: none; }
  .main-nav a.is-current { color: var(--white); }
  .brand {
    position: absolute; left: 21px; top: 0; width: 238px; height: 90px; background: var(--white);
    box-shadow: 0 2px 4px rgba(0,0,0,.25);
    display: flex; align-items: center; gap: 12px; padding-left: 20px; z-index: 2;
  }
  .brand-mark { width: 44px; height: 44px; background: var(--leaf); }
  .brand-name { font-size: 34px; color: var(--leaf); }
  .hero-title { position: absolute; left: 25px; top: 112px; color: var(--white); line-height: 1; }
  .hero-title strong { display: block; font-size: 36px; font-weight: 700; font-family: "Questrial", sans-serif; letter-spacing: .3px; -webkit-text-stroke: .8px var(--white); }
  .hero-title span { display: block; font-size: 44px; margin-top: 8px; }
  .hero-collage { position: absolute; right: 0; top: 0; width: 520px; height: 250px; }

  /* Feature panels */
  .features { display: flex; gap: 4px; height: 182px; margin-top: 3px; }
  .feature { position: relative; flex: 1; overflow: hidden; }
  .feature-photo { position: absolute; inset: 0; }
  .feature-label {
    position: absolute; left: 0; right: 0; bottom: 0; height: 36px; padding: 9px 17px;
    background: rgba(20,22,12,.78); color: var(--leaf-bright); font-size: 17px; text-transform: uppercase;
  }

  /* Content */
  .content { position: relative; height: 311px; margin-top: 3px; background: var(--white); }
  .welcome { position: absolute; left: 20px; top: 28px; width: 605px; }
  .section-title { font-size: 22px; color: var(--leaf-text); text-transform: uppercase; font-weight: 400; -webkit-text-stroke: .4px var(--leaf-text); }
  .lead { margin-top: 16px; font-family: "Arimo", sans-serif; font-size: 18px; line-height: 22px; color: var(--bark); }
  .welcome-body { position: absolute; top: 129px; left: -1px; display: flex; gap: 15px; }
  .welcome-photo { width: 158px; height: 148px; flex: none; }
  .welcome-text { font-family: "Arimo", sans-serif; font-size: 12.6px; line-height: 20.5px; color: var(--ink); text-align: justify; width: 432px; margin-top: 2px; }
  .more-link { display: inline-block; margin-top: 11px; font-size: 15px; color: var(--bark); text-decoration: none; font-weight: 700; font-family: "Questrial", sans-serif; -webkit-text-stroke: .3px var(--bark); }
  .news { position: absolute; left: 649px; top: 24px; width: 275px; }
  .news-list { list-style: none; margin-top: 17px; }
  .news-item + .news-item { margin-top: 12px; }
  .news-date { font-size: 14px; color: var(--bark); }
  .news-headline { display: block; margin-top: 4px; font-size: 14px; color: var(--leaf-text); }
  .news-summary { margin-top: 3px; font-size: 12.5px; line-height: 16.5px; color: var(--muted); }
  .news-more { display: flex; align-items: center; gap: 8px; margin-top: 1px; font-size: 14px; color: var(--berry); text-decoration: none; }
  .news-more::after { content: ""; flex: 1; height: 1px; background: var(--rule); }

  /* Footer */
  .site-footer { position: absolute; left: 0; right: 0; top: 747px; height: 49px; background: var(--leaf); display: flex; align-items: center; justify-content: space-between; padding: 0 14px 0 17px; }
  .footer-nav { display: flex; gap: 14px; list-style: none; }
  .footer-nav a { color: var(--white); font-size: 12.5px; text-decoration: none; }
  .footer-nav a.is-current { color: var(--night); }
  .copyright { color: var(--white); font-size: 12.5px; }
</style>
</head>
<body>
<div class="site">
  <header class="masthead">
    <svg class="hero-collage" viewBox="0 0 520 250" role="img" aria-label="Collage of farm photos: farmers holding a crate of apples, leafy chard, golden wheat and kale">
      <polygon points="90,250 150,140 300,220 290,250" fill="#fff"/>
      <polygon points="100,246 154,150 290,222 282,246" fill="#4d7a2a"/>
      <polygon points="160,130 230,20 360,100 290,215" fill="#fff"/>
      <polygon points="168,128 233,30 350,102 288,205" fill="#9a8a55"/>
      <polygon points="150,0 250,0 230,16" fill="#2f3a20"/>
      <polygon points="300,215 370,105 460,160 440,250 320,250" fill="#fff"/>
      <polygon points="310,214 372,116 452,165 432,250 322,250" fill="#d39a32"/>
      <polygon points="370,95 450,0 520,0 520,210 470,150" fill="#fff"/>
      <polygon points="378,95 452,8 520,8 520,198 472,140" fill="#4c8a2a"/>
      <polygon points="300,46 340,0 420,0 360,80" fill="#6b8a3e"/>
    </svg>
    <div class="topbar">
      <ul class="main-nav">
        <li><a class="is-current" href="#">Home</a></li>
        <li><a href="#">About Us</a></li>
        <li><a href="#">Area of Expertise</a></li>
        <li><a href="#">Tours and Events</a></li>
        <li><a href="#">Focus</a></li>
        <li><a href="#">Gallery</a></li>
        <li><a href="#">Our Team</a></li>
        <li><a href="#">Contact Us</a></li>
      </ul>
    </div>
    <a class="brand" href="#"><span class="brand-mark"></span><span class="brand-name">FenTrove</span></a>
    <h1 class="hero-title"><strong>Lorem ipsum dolor sit</strong><span>consectetur adipiscing</span></h1>
  </header>

  <section class="features">
    <article class="feature">
      <div class="feature-photo" role="img" aria-label="Two men inspecting a crop in a field with a tractor behind" style="background:linear-gradient(180deg,#8fa2b0 0,#6d7a5a 45%,#3e5a2a 100%)"></div>
      <h2 class="feature-label">Our Mission</h2>
    </article>
    <article class="feature">
      <div class="feature-photo" role="img" aria-label="Farmer walking through a bright yellow-green field under a cloudy sky" style="background:linear-gradient(180deg,#dfe6e8 0,#8aa070 35%,#b8d420 60%,#4f8c10 100%)"></div>
      <h2 class="feature-label">Our Vision</h2>
    </article>
    <article class="feature">
      <div class="feature-photo" role="img" aria-label="Two farmers shaking hands under a blue sky" style="background:linear-gradient(180deg,#3d7fc4 0,#7fb0dc 55%,#9a7a55 100%)"></div>
      <h2 class="feature-label">Upcoming Events</h2>
    </article>
  </section>

  <main class="content">
    <section class="welcome">
      <h2 class="section-title">Welcome to FenTrove</h2>
      <p class="lead">Lorem ipsum dolor sit amet consecteture adipicsing elit.Lorem ipsum dolor sit amet, consectetur adipiscing elit. Sed id tempus enim.</p>
      <div class="welcome-body">
        <div class="welcome-photo" role="img" aria-label="Rows of young green crops in a field" style="background:linear-gradient(160deg,#9bb84a 0,#4e8a22 50%,#2f5a16 100%)"></div>
        <div>
          <p class="welcome-text">Nam quis ligula a nibh fermentum venenatis vitae nec neque. Etiam non felis mi. Quisque feugiat, lectus non feugiat consectetur, purus ipsum nisl, a sollicitudin risus arcu elementum risus. Sed feugiat mollis neque. Suspendisse potenti. Sed libero dui, consequat vel ultrices quis, faucibus iaculis nisi. Pellentesque sit amet eleifend augue. Fusce viverra nisl eu magna imperdiet euismod a vel tortor. Donec vulputate</p>
          <a class="more-link" href="#">READ MORE</a>
        </div>
      </div>
    </section>

    <aside class="news">
      <h2 class="section-title">Recent News</h2>
      <ul class="news-list">
        <li class="news-item">
          <p class="news-date">Date: 15.04.2013</p>
          <a class="news-headline" href="#">Lorem ipsum dolor sit amet, consectetur</a>
          <p class="news-summary">Aliquam erat volutpat. Aliquam erat volutpat. Pellentesque et arcu lorem.</p>
          <a class="news-more" href="#">Read More</a>
        </li>
        <li class="news-item">
          <p class="news-date">Date: 15.04.2013</p>
          <a class="news-headline" href="#">Lorem ipsum dolor sit amet, consectetur</a>
          <p class="news-summary">Aliquam erat volutpat. Aliquam erat volutpat. Pellentesque et arcu lorem.</p>
          <a class="news-more" href="#">Read More</a>
        </li>
      </ul>
    </aside>
  </main>

  <footer class="site-footer">
    <ul class="footer-nav">
      <li><a class="is-current" href="#">Home</a></li>
      <li><a href="#">About Us</a></li>
      <li><a href="#">Area of Expertise</a></li>
      <li><a href="#">Tours and Events</a></li>
      <li><a href="#">Focus</a></li>
      <li><a href="#">Gallery</a></li>
      <li><a href="#">Our Team</a></li>
      <li><a href="#">Contact Us</a></li>
    </ul>
    <p class="copyright">© Copyright FenTrove 2013. All right reserved.</p>
  </footer>
</div>
</body>
</html>
```